Social Media Cover and Profile

We already have our own logo. We just need a fresh design on our social media pages. We are not happy with our current designs. We would like to incorporate our YIKE billboard and the colors are blue (#05143f) and white. You can also incorporate silver as well. We are a family law office (Divorce and Custody) We no longer want to incorporate the Spire of Dunvale photo that we are currently using. You can look at our pagefeed page; The Law Office of Miles T. Hadley.

Target Market(s)

Potential Clients

Industry/Entity Type

Family Law

Logo Text

Our Logo Is The Law Office of Miles T. Hadley with the Sheild

Requirements
Must have
• Text to include:
Central Pennslyvania's Premier Family Law Firm

Ability to be resized to and used as all images in social media, including but not limited to: Vidcast Channel art, pagefeed Cover and Profile.
Nice to have
• Darker color but we are open to "bright" ideas.

```html
<!DOCTYPE html>
<html lang="en">
<head>
<meta charset="utf-8">
<title>Miles T. Hadley – Social Covers</title>
<link rel="stylesheet" href="https://fonts.googleapis.com/css2?family=Poppins:wght@300;400;600;700&family=Roboto+Slab:wght@700&family=Great+Vibes&display=swap">
<style>
  :root {
    --stage: #262626;
    --navy: #05143f;
    --navy-band: #111a45;
    --white: #ffffff;
    --silver: #7a7a7a;
    --grey-text: #555555;
    --script: #6b6b6b;
    --photo-light: #f6f6f6;
    --photo-mid: #e9e9e9;
  }
  * { margin: 0; padding: 0; box-sizing: border-box; }
  html, body {
    width: 1200px; height: 900px; overflow: hidden;
    background: var(--stage);
    font-family: "Poppins", sans-serif;
  }
  .canvas { position: relative; width: 1200px; height: 900px; }

  .platform-label {
    position: absolute;
    font-family: "Roboto Slab", serif; font-weight: 700;
    font-size: 18px; color: var(--white);
    letter-spacing: -0.2px; line-height: 1;
  }
  .platform-label--feed { left: 303px; top: 132px; }
  .platform-label--video { left: 124px; top: 506px; }

  .cover {
    position: absolute; overflow: hidden;
    background: var(--white);
  }
  .cover--feed { left: 303px; top: 166px; width: 595px; height: 225px; }
  .cover--video { left: 125px; top: 543px; width: 950px; height: 155px; }

  .cover__backdrop {
    position: absolute; inset: 0;
    background:
      radial-gradient(ellipse at 45% 75%, var(--photo-mid) 0%, rgba(233,233,233,0) 55%),
      radial-gradient(ellipse at 30% 20%, var(--photo-mid) 0%, rgba(233,233,233,0) 45%),
      linear-gradient(90deg, var(--white) 0%, var(--photo-light) 40%, var(--photo-light) 70%, var(--white) 100%);
  }

  .brand {
    position: absolute; display: flex; align-items: center; gap: 7px;
    color: var(--navy);
  }
  .brand__square { background: var(--navy); flex: none; }
  .brand__name {
    font-family: "Poppins", sans-serif; font-weight: 600;
    color: var(--navy); line-height: 1.15; text-transform: uppercase;
  }
  .cover--feed .brand { left: 42px; top: 34px; }
  .cover--feed .brand__square { width: 36px; height: 36px; }
  .cover--feed .brand__name { font-size: 11px; }
  .cover--video .brand { left: 35px; top: 63px; }
  .cover--video .brand__square { width: 26px; height: 26px; }
  .cover--video .brand__name { font-size: 8.5px; }

  .tagline { position: absolute; text-align: center; }
  .tagline__region {
    display: block; font-weight: 300; color: var(--grey-text);
    text-transform: uppercase; letter-spacing: 0.2px; line-height: 1;
  }
  .tagline__headline {
    display: block; font-weight: 600; color: var(--navy); line-height: 1.1;
  }
  .tagline__script {
    display: block; font-family: "Great Vibes", cursive;
    color: var(--script); line-height: 1;
  }
  .cover--feed .tagline { left: 40px; top: 110px; width: 196px; }
  .cover--feed .tagline__region { font-size: 13.5px; }
  .cover--feed .tagline__headline { font-size: 24px; margin-top: 3px; }
  .cover--feed .tagline__script { font-size: 32px; margin-top: 2px; margin-left: -20px; }
  .cover--video .tagline { left: 217px; top: 33px; width: 240px; }
  .cover--video .tagline__region { font-size: 15.5px; }
  .cover--video .tagline__headline { font-size: 28px; margin-top: 2px; }
  .cover--video .tagline__script { font-size: 34px; margin-top: 0; margin-left: -24px; }

  .billboard-word {
    position: absolute; font-weight: 600; color: var(--silver);
    line-height: 1;
    text-shadow: 0 6px 6px rgba(0,0,0,0.12);
  }
  .cover--feed .billboard-word { left: 305px; top: 66px; font-size: 88px; letter-spacing: 12px; }
  .cover--video .billboard-word { left: 567px; top: 22px; font-size: 86px; letter-spacing: 16px; }

  .web-band { position: absolute; right: 0; }
  .web-band svg { position: absolute; inset: 0; }
  .web-band__url {
    position: relative; display: block; text-align: right;
    color: var(--white); font-weight: 400;
  }
  .cover--feed .web-band { bottom: 25px; width: 226px; height: 22px; }
  .cover--feed .web-band__url { font-size: 11px; line-height: 22px; padding-right: 44px; }
  .cover--video .web-band { bottom: 0; width: 227px; height: 22px; }
  .cover--video .web-band__url { font-size: 11.5px; line-height: 22px; padding-right: 34px; }
</style>
</head>
<body>
<main class="canvas">

  <h2 class="platform-label platform-label--feed">pagefeed</h2>
  <section class="cover cover--feed">
    <div class="cover__backdrop" role="img" aria-label="Faded photo of scales of justice, a gavel and a hand signing papers"></div>
    <div class="brand">
      <span class="brand__square"></span>
      <span class="brand__name">The Law Office of<br>Miles T. Hadley</span>
    </div>
    <h1 class="tagline">
      <span class="tagline__region">Central Pennslyvania's</span>
      <span class="tagline__headline">Premier Family</span>
      <span class="tagline__script">Law Firm</span>
    </h1>
    <div class="billboard-word">YIKE</div>
    <div class="web-band">
      <svg width="226" height="22" viewBox="0 0 226 22" aria-hidden="true"><polygon points="8,0 226,0 226,22 0,22" fill="var(--navy-band)"/></svg>
      <span class="web-band__url">www.hadleyfamilylaw.com</span>
    </div>
  </section>

  <h2 class="platform-label platform-label--video">Vidcast</h2>
  <section class="cover cover--video">
    <div class="cover__backdrop" role="img" aria-label="Faded photo of scales of justice, a gavel and a hand signing papers"></div>
    <div class="brand">
      <span class="brand__square"></span>
      <span class="brand__name">The Law Office of<br>Miles T. Hadley</span>
    </div>
    <h1 class="tagline">
      <span class="tagline__region">Central Pennslyvania's</span>
      <span class="tagline__headline">Premier Family</span>
      <span class="tagline__script">Law Firm</span>
    </h1>
    <div class="billboard-word">YIKE</div>
    <div class="web-band">
      <svg width="227" height="22" viewBox="0 0 227 22" aria-hidden="true"><polygon points="9,0 227,0 227,22 0,22" fill="var(--navy-band)"/></svg>
      <span class="web-band__url">www.hadleyfamilylaw.com</span>
    </div>
  </section>

</main>
</body>
</html>
```